MBW Website

I'm looking to design a 1 page website for my email marketing business called 'Inbox Harvest Works.' The business will be designed to attract eCommerce clients in particular.

It will be a very simple website with my picture, a Subscribe area to capture email addresses (and send out lead magnet PDFs), and some basic copy and social media links, nothing fancy!

I will provide the profile picture and all related copy, looking to use the color green and have it fill up the entire screen.

Here's an example of a similar site I really like:

http://prosecraftacademy-example.com/

I'm just looking for the site to provide information about my email marketing services and make a personal connection with the site visitors.

Target Market(s)

eCommerce businesse customers

Industry/Entity Type

Business

Number of Pages Required

1 page

Font styles to use
Sans Serif

Colors
00a990
33b8a4
87cfc6
cfeae6

Requirements
Must have
• Hosted on HostMoor serviers (we can discuss this*)
• Full page layout (no left/right margins)
• Profile picture / Subscribe and Lead Magnet section above the fold
• Ability for me to supply all copy (against white background)
• Friendloop / Chirply / WorkNest social media icons at the bottom
• Footer section with simple text I will provide

```html
<!DOCTYPE html>
<html lang="en">
<head>
<meta charset="utf-8">
<title>MBW — Inbox Harvest Works</title>
<link rel="stylesheet" href="https://fonts.googleapis.com/css2?family=Nunito+Sans:wght@300;400;600;700&family=Open+Sans:wght@400&display=swap">
<style>
  :root {
    --green-deep: #00a990;
    --green: #33b8a4;
    --green-soft: #87cfc6;
    --green-pale: #cfeae6;
    --white: #ffffff;
    --ink: #454545;
    --ink-muted: #8a8a8a;
    --rule: #b9b9b9;
    --rule-strong: #a6a6a6;
    --footer-bg: #e8e8e8;
    --accent: #e8b400;
    --chirply: #55acee;
    --friendloop: #3b5998;
    --worknest: #0077b5;
  }
  * { box-sizing: border-box; margin: 0; padding: 0; }
  html, body { width: 1200px; height: 1086px; overflow: hidden; background: var(--white); }
  body { position: relative; font-family: "Open Sans", sans-serif; }

  .hero { position: absolute; left: 0; top: 0; width: 1200px; height: 680px; }
  .hero-art { position: absolute; inset: 0; }

  .brand {
    position: absolute; left: 101px; top: 30px;
    font-family: "Nunito Sans", sans-serif; font-weight: 400;
    font-size: 62px; line-height: 70px; color: var(--white); letter-spacing: 1px;
  }

  .hero-copy { position: absolute; left: 579px; top: 214px; width: 540px; color: var(--white); }
  .hero-title {
    font-family: "Nunito Sans", sans-serif; font-weight: 700;
    font-size: 42px; line-height: 48px; letter-spacing: 0.3px;
  }
  .hero-lead {
    margin: 9px 0 0 5px;
    font-family: "Nunito Sans", sans-serif; font-weight: 400;
    font-size: 16px; line-height: 26px;
  }

  .subscribe { position: absolute; left: 587px; top: 395px; display: flex; height: 44px; }
  .subscribe-field {
    width: 351px; height: 44px; background: var(--white);
    display: flex; align-items: center; padding-left: 16px; gap: 10px;
    font-family: "Nunito Sans", sans-serif; font-size: 17px; color: #8f8f8f;
  }
  .subscribe-button {
    width: 127px; height: 44px; background: var(--accent); color: var(--white);
    border: 0; font-family: "Nunito Sans", sans-serif; font-weight: 600; font-size: 19px;
  }

  .welcome { position: absolute; left: 0; top: 686px; width: 1200px; text-align: center; }
  .welcome-title {
    font-family: "Nunito Sans", sans-serif; font-weight: 300;
    font-size: 35px; line-height: 46px; color: var(--ink); letter-spacing: 0.6px;
  }
  .welcome-rule { position: relative; width: 180px; height: 2px; margin: 11px auto 0; background: var(--rule); }
  .welcome-rule::after {
    content: ""; position: absolute; left: 73px; top: -2px; width: 36px; height: 4px; background: var(--rule-strong);
  }
  .welcome-text {
    width: 860px; margin: 12px auto 0;
    font-size: 17px; line-height: 28px; color: var(--ink-muted);
  }

  .site-footer {
    position: absolute; left: 0; top: 946px; width: 1200px; height: 140px;
    background: var(--footer-bg); text-align: center;
  }
  .footer-note {
    margin-top: 35px; font-family: "Nunito Sans", sans-serif;
    font-size: 15.5px; color: #7d7d7d; word-spacing: 1px;
  }
  .social { display: flex; justify-content: center; gap: 22px; margin-top: 20px; list-style: none; }
  .social-item {
    display: flex; align-items: center; gap: 7px;
    font-family: "Nunito Sans", sans-serif; font-size: 14px; color: #6f6f6f;
  }
  .social-dot { width: 32px; height: 32px; border-radius: 50%; border: 2px solid var(--white); }
  .dot-chirply { background: var(--chirply); }
  .dot-friendloop { background: var(--friendloop); }
  .dot-worknest { background: var(--worknest); }
</style>
</head>
<body>
  <header class="hero">
    <svg class="hero-art" width="1200" height="680" viewBox="0 0 1200 680">
      <defs>
        <linearGradient id="heroGreen" x1="0" y1="0" x2="1" y2="1">
          <stop offset="0" stop-color="#3cbfa9"/>
          <stop offset="0.5" stop-color="#33b8a4"/>
          <stop offset="1" stop-color="#1fa88e"/>
        </linearGradient>
        <linearGradient id="portraitTone" x1="0" y1="0" x2="0" y2="1">
          <stop offset="0" stop-color="#9fb8ad"/>
          <stop offset="1" stop-color="#6f7a74"/>
        </linearGradient>
      </defs>
      <rect width="1200" height="680" fill="url(#heroGreen)"/>
      <rect role="img" aria-label="Portrait photo of the business owner" x="160" y="95" width="430" height="585" fill="url(#portraitTone)"/>
      <path d="M0 667 Q600 529 1200 667 L1200 680 L0 680 Z" fill="var(--white)"/>
      <path d="M0 662 Q600 512 1200 662" fill="none" stroke="var(--green-soft)" stroke-width="2"/>
      <path d="M0 676 Q600 546 1200 676" fill="none" stroke="var(--green-pale)" stroke-width="2"/>
    </svg>

    <div class="brand">MBW</div>

    <div class="hero-copy">
      <h1 class="hero-title">Donec dictum lectus non<br>Cras ante vitae enim</h1>
      <p class="hero-lead">Altricies massa est sed nisl Class aptent taciti sociosqu ad litora<br>torquent per conubia nostra per inceptos hymenaeos</p>
    </div>

    <form class="subscribe">
      <label class="subscribe-field">
        <svg width="24" height="18" viewBox="0 0 24 18" aria-hidden="true">
          <rect x="0" y="0" width="24" height="18" rx="2" fill="#c9c9c9"/>
          <path d="M1 2 L12 10 L23 2" fill="none" stroke="#ffffff" stroke-width="2"/>
        </svg>
        <span>Enter Email address</span>
      </label>
      <button class="subscribe-button" type="button">Susbcribe</button>
    </form>
  </header>

  <section class="welcome">
    <h2 class="welcome-title">Welcome to Inbox Harvest Works</h2>
    <div class="welcome-rule"></div>
    <p class="welcome-text">Auscipit leo massa sodales velit et scelerisque mi tortor at ipsum cligula augue bibendum accumsan vestibulum ut commodo a mi Morbi ornare gravida elit Integer congue augue et malesuada iaculis ipsum dui aliquet felis at cursus magna nisl nec elit Praesent elementum elit at tellus nec ultricies sit amet porttitor mattis enim In massa libero interdum nec interdum vel blandit sed nulla</p>
  </section>

  <footer class="site-footer">
    <p class="footer-note">© 2017 Company Name &nbsp;All right reserved &nbsp;Term of Use</p>
    <ul class="social">
      <li class="social-item"><span class="social-dot dot-chirply"></span>Chirply</li>
      <li class="social-item"><span class="social-dot dot-friendloop"></span>Friendloop</li>
      <li class="social-item"><span class="social-dot dot-worknest"></span>WorkNest</li>
    </ul>
  </footer>
</body>
</html>
```